Legal Services Power Point

Need a PP template for a legal consulting company - we prefer the use of our logo colors. Also- emphasis on international/global business with images of the USA because we serve immigration and international business coming to the US and we will use the PP to make presentations in other countries. The Company is Merivale Law Firm PC ( logo uploaded) but we have do business outside the US as Merivale Consulting Group ( logo upoaded too)

Target Market(s)

Business clients

Industry/Entity Type

Legal/ International Cross-Border/ Immigration

Font styles to use
Sans Serif

Colors
0054AA
0677BA
7BADD7
CADEEF
E8F1F8

Requirements
Must have
• International elements, global, US, we do immigration and legal consulting for foreign business
Nice to have
• Make it look elegant as we are in the legal and consulting business.

```html
<!DOCTYPE html>
<html lang="en">
<head>
<meta charset="utf-8">
<title>Merivale Law Firm PC – Presentation Template</title>
<link href="https://fonts.googleapis.com/css2?family=Montserrat:wght@300;400;600;700;800&display=swap" rel="stylesheet">
<style>
:root{
  --deep:#0a3a78;
  --blue:#0054AA;
  --blue-mid:#0677BA;
  --sky:#7BADD7;
  --pale:#CADEEF;
  --mist:#E8F1F8;
  --paper:#ffffff;
  --stage:#e4e6ea;
  --ink:#26303f;
  --grey:#7f8896;
  --flag-red:#b3282d;
}
*{margin:0;padding:0;box-sizing:border-box}
html,body{width:1200px;height:2448px;overflow:hidden}
body{background:var(--stage);font-family:"Montserrat",Arial,sans-serif;color:var(--ink);position:relative}
.abs{position:absolute}
.slide{position:absolute;background:var(--paper);overflow:hidden;box-shadow:0 4px 14px rgba(0,0,0,.12)}
.grid .slide{width:520px;height:270px}
.band{position:absolute;left:0;top:0;background:linear-gradient(90deg,var(--deep),var(--blue) 60%,var(--blue-mid))}
.band-title{position:absolute;color:#fff;font-weight:800;letter-spacing:.5px}
.photo{position:absolute}
.ph-city{background:linear-gradient(180deg,var(--blue-mid) 0%,var(--blue) 50%,var(--deep) 100%)}
.ph-tower{background:linear-gradient(160deg,var(--mist),var(--pale) 50%,var(--sky))}
.ph-justice{background:linear-gradient(90deg,rgba(0,84,170,0),#7a8fa8 45%,#3d5878)}
.ph-liberty{background:linear-gradient(135deg,var(--pale),#8fb3a8)}
.ph-globe{background:linear-gradient(135deg,var(--mist),var(--sky))}
.ph-passport{background:linear-gradient(135deg,#3a5f8f,var(--deep))}
.ph-person{background:linear-gradient(180deg,#dcdde2,#9ea4ae)}
.ph-gavel{background:linear-gradient(135deg,var(--flag-red) 0%,#7a2a28 35%,#3a2a22 65%,var(--deep) 100%)}
.corner{position:absolute;width:28px;height:28px;border-color:var(--blue);border-style:solid;border-width:0}
.corner.tl{border-top-width:5px;border-left-width:5px}
.corner.br{border-bottom-width:5px;border-right-width:5px}
.corner.bl{border-bottom-width:5px;border-left-width:5px}
.corner.tr{border-top-width:5px;border-right-width:5px}
.corner.light{border-color:#fff}
.brand{position:absolute;display:flex;flex-direction:column;align-items:center;gap:3px;color:var(--blue);font-weight:700;text-align:center}
.brand .mark{background:var(--blue)}
.para{position:absolute;font-size:5.5px;line-height:1.6;color:var(--grey)}
.h-small{position:absolute;font-size:7px;font-weight:700;color:var(--blue)}
.title{position:absolute;font-weight:800;color:var(--blue)}
.step{height:50px;color:#fff;font-size:6px;padding:8px}
.step.a{background:var(--blue)}
.step.b{background:var(--blue-mid)}
.contact-list{color:var(--blue)}
.contact-list span{color:var(--ink)}
</style>
</head>
<body>

<section class="stack">
  <div class="slide" style="left:120px;top:40px;width:760px;height:420px">
    <div class="band" style="width:760px;height:130px"></div>
    <div class="band-title" style="left:40px;top:48px;font-size:30px">OUR PROCESS</div>
    <div class="photo ph-justice" role="img" aria-label="Lady justice statue before a US city skyline" style="left:440px;top:0;width:320px;height:130px;opacity:.8"></div>
  </div>
  <div class="slide" style="left:180px;top:230px;width:760px;height:420px">
    <div class="title" style="left:40px;top:60px;font-size:30px">OUR SERVICES</div>
    <div class="abs" style="left:40px;top:112px;font-size:14px;font-weight:600">Over <b style="color:var(--blue)">20 years</b> of Success Stories</div>
    <div class="abs" style="left:400px;top:40px;font-size:11px;line-height:30px;color:var(--grey)">▪ Corporate &amp; Business Formation<br>▪ Immigration &amp; Investor Visas<br>▪ Contracts &amp; Negotiation</div>
  </div>
  <div class="slide" style="left:240px;top:420px;width:760px;height:420px">
    <div class="band" style="width:760px;height:110px"></div>
    <div class="band-title" style="left:40px;top:40px;font-size:30px">ABOUT US</div>
    <div class="abs" style="left:40px;top:140px;font-size:13px;font-weight:600">A one-stop shop law firm for all<br>of your Business needs.</div>
  </div>
  <div class="slide" style="left:300px;top:620px;width:780px;height:470px">
    <div class="photo ph-city" role="img" aria-label="New York skyline with silhouettes of international business people" style="left:0;top:0;width:780px;height:320px"></div>
    <div class="abs" style="left:0;top:110px;width:780px;text-align:center;color:var(--pale);font-size:26px;font-weight:300;letter-spacing:3px">NAVIGATING BORDERS</div>
    <div class="abs" style="left:0;top:146px;width:780px;text-align:center;color:#fff;font-size:44px;font-weight:800;letter-spacing:1px">SECURING FUTURES</div>
    <div class="corner tl light" style="left:30px;top:30px;width:60px;height:60px;border-top-width:8px;border-left-width:8px"></div>
    <div class="corner br light" style="right:30px;top:250px;width:60px;height:60px;border-bottom-width:8px;border-right-width:8px"></div>
    <div class="corner bl" style="left:30px;bottom:24px;width:60px;height:60px;border-bottom-width:8px;border-left-width:8px"></div>
    <div class="brand" style="left:260px;top:338px;width:120px;font-size:12px"><span class="mark" style="width:36px;height:36px"></span>MERIVALE<span style="font-size:7px;font-weight:400">LAW FIRM PC</span></div>
    <div class="brand" style="left:400px;top:338px;width:140px;font-size:12px"><span class="mark" style="width:36px;height:36px"></span>MERIVALE<span style="font-size:7px;font-weight:400">CONSULTING GROUP</span></div>
  </div>
</section>

<section class="grid">
  <div class="slide" style="left:48px;top:1240px">
    <div class="photo ph-city" role="img" aria-label="New York skyline with silhouettes of international business people" style="left:0;top:0;width:520px;height:180px"></div>
    <div class="abs" style="left:0;top:54px;width:520px;text-align:center;color:var(--pale);font-size:17px;font-weight:300;letter-spacing:2px">NAVIGATING BORDERS</div>
    <div class="abs" style="left:0;top:76px;width:520px;text-align:center;color:#fff;font-size:28px;font-weight:800">SECURING FUTURES</div>
    <div class="corner tl light" style="left:18px;top:18px"></div>
    <div class="corner bl" style="left:18px;bottom:14px"></div>
    <div class="corner br light" style="right:18px;top:140px"></div>
    <div class="brand" style="left:172px;top:190px;width:80px;font-size:8px"><span class="mark" style="width:22px;height:22px"></span>MERIVALE<span style="font-size:5px;font-weight:400">LAW FIRM PC</span></div>
    <div class="brand" style="left:262px;top:190px;width:90px;font-size:8px"><span class="mark" style="width:22px;height:22px"></span>MERIVALE<span style="font-size:5px;font-weight:400">CONSULTING GROUP</span></div>
  </div>

  <div class="slide" style="left:632px;top:1240px">
    <div class="band" style="width:340px;height:60px"></div>
    <div class="band-title" style="left:24px;top:20px;font-size:17px">ABOUT US</div>
    <div class="photo ph-tower" role="img" aria-label="Glass office towers of a US city seen from below" style="left:340px;top:0;width:180px;height:270px"></div>
    <div class="corner tr light" style="right:14px;top:14px"></div>
    <div class="abs" style="left:24px;top:78px;font-size:8px;font-weight:600;color:var(--blue);line-height:1.4">A one-stop shop law firm for all of<br>your Business/Immigration needs.</div>
    <div class="para" style="left:24px;top:110px;width:290px">We guide companies and families across borders with clear counsel on visas, investment, formation and compliance. Our attorneys work in several languages and partner with clients from the first question to the final approval.<br><br>From startups entering the US market to global firms moving key staff, we build a plan that fits each goal, timeline and budget, and we stay close at every step of the way.</div>
  </div>

  <div class="slide" style="left:48px;top:1540px">
    <div class="title" style="left:24px;top:92px;font-size:17px">OUR SERVICES</div>
    <div class="abs" style="left:24px;top:120px;font-size:7.5px;line-height:1.5;width:190px">Over <b style="color:var(--blue)">20 years</b> of Success Stories in Immigration and Corporate Law</div>
    <div class="abs" style="left:280px;top:36px;width:210px;font-size:6px;color:var(--grey)">
      <div style="line-height:20px">▪ Business Formation &amp; Setup</div>
      <div style="line-height:20px">▪ Investor &amp; Treaty Visas</div>
      <div style="line-height:20px">▪ Employment Based Visas</div>
      <div style="line-height:20px;background:var(--blue);color:#fff;padding-left:6px">▪ Contracts &amp; Negotiation</div>
      <div style="line-height:20px">▪ Family Immigration</div>
      <div style="line-height:20px">▪ Compliance &amp; Audits</div>
      <div style="line-height:20px">▪ Mergers &amp; Acquisitions</div>
      <div style="line-height:20px">▪ Citizenship</div>
    </div>
    <div class="corner tl" style="left:14px;top:14px"></div>
    <div class="corner br" style="right:14px;bottom:14px"></div>
  </div>

  <div class="slide" style="left:632px;top:1540px">
    <div class="band" style="width:520px;height:120px"></div>
    <div class="photo ph-justice" role="img" aria-label="Lady justice statue against a US city skyline" style="left:200px;top:0;width:320px;height:120px;opacity:.75"></div>
    <div class="band-title" style="left:24px;top:22px;font-size:17px">OUR PROCESS</div>
    <div class="abs" style="left:70px;top:120px;display:grid;grid-template-columns:repeat(3,118px);gap:8px">
      <div class="step a"><b>Consultation</b><br>Review goals</div>
      <div class="step b"><b>Strategy</b><br>Build the plan</div>
      <div class="step a"><b>Documents</b><br>Gather records</div>
      <div class="step b"><b>Filing</b><br>Submit the case</div>
      <div class="step a"><b>Follow-up</b><br>Track progress</div>
      <div class="step b"><b>Approval</b><br>Next steps</div>
    </div>
  </div>

  <div class="slide" style="left:48px;top:1840px">
    <div class="title" style="left:24px;top:26px;font-size:16px">SLIDE HEADER</div>
    <div class="corner tr" style="right:14px;top:14px"></div>
    <div class="photo ph-globe" role="img" aria-label="Globe and world map on a business desk" style="left:24px;top:62px;width:150px;height:84px"></div>
    <div class="photo ph-liberty" role="img" aria-label="Statue of Liberty" style="left:185px;top:62px;width:150px;height:84px"></div>
    <div class="photo ph-passport" role="img" aria-label="US passport and travel papers" style="left:346px;top:62px;width:150px;height:84px"></div>
    <div class="h-small" style="left:24px;top:156px">Global Reach</div>
    <div class="h-small" style="left:185px;top:156px">Clear Contracts</div>
    <div class="h-small" style="left:346px;top:156px">Smooth Travel</div>
    <div class="para" style="left:24px;top:170px;width:150px">Counsel for clients moving into US markets from abroad.</div>
    <div class="para" style="left:185px;top:170px;width:150px">Agreements written to protect your interests.</div>
    <div class="para" style="left:346px;top:170px;width:150px">Visa planning that keeps your team moving.</div>
  </div>

  <div class="slide" style="left:632px;top:1840px">
    <div class="title" style="left:24px;top:26px;font-size:16px">OUR TEAM</div>
    <div class="corner tr" style="right:14px;top:14px"></div>
    <div class="photo ph-person" role="img" aria-label="Portrait of team member" style="left:24px;top:62px;width:110px;height:110px"></div>
    <div class="photo ph-person" role="img" aria-label="Portrait of team member" style="left:144px;top:62px;width:110px;height:110px"></div>
    <div class="photo ph-person" role="img" aria-label="Portrait of team member" style="left:264px;top:62px;width:110px;height:110px"></div>
    <div class="photo ph-person" role="img" aria-label="Portrait of team member" style="left:384px;top:62px;width:110px;height:110px"></div>
    <div class="abs" style="left:24px;top:172px;width:470px;height:20px;background:var(--blue);display:grid;grid-template-columns:repeat(4,1fr);color:#fff;font-size:6px;font-weight:600;text-align:center;line-height:20px"><span>Nora Hale</span><span>Celia Marsh</span><span>Ada Quinn</span><span>Ines Ward</span></div>
    <div class="abs" style="left:24px;top:196px;width:470px;display:grid;grid-template-columns:repeat(4,1fr);color:var(--grey);font-size:5px;text-align:center"><span>Managing Partner</span><span>Senior Attorney</span><span>Immigration Lead</span><span>Legal Advisor</span></div>
  </div>

  <div class="slide" style="left:48px;top:2140px">
    <div class="title" style="left:24px;top:30px;font-size:16px">SLIDE TITLE HERE</div>
    <div class="abs" style="left:24px;top:58px;font-size:7px;font-weight:600;color:var(--blue)">Trusted by clients worldwide</div>
    <div class="para" style="left:24px;top:72px;width:220px">We serve founders, investors and families from over thirty countries who plan to live, work or build a company in the US.</div>
    <div class="abs" style="left:24px;top:124px;font-size:13px;font-weight:800;color:var(--blue)">61%</div>
    <div class="para" style="left:70px;top:127px;width:170px">of clients come from outside the US</div>
    <div class="abs" style="left:24px;top:150px;font-size:13px;font-weight:800;color:var(--blue)">95%</div>
    <div class="para" style="left:70px;top:153px;width:170px">approval rate on filed cases</div>
    <div class="corner bl" style="left:14px;bottom:14px"></div>
    <div class="photo ph-gavel" role="img" aria-label="Gavel in front of an American flag" style="left:260px;top:0;width:260px;height:270px"></div>
  </div>

  <div class="slide" style="left:632px;top:2140px">
    <div class="band" style="width:520px;height:46px"></div>
    <div class="band-title" style="left:0;top:14px;width:520px;text-align:center;font-size:15px">WE'RE HERE TO HELP!</div>
    <div class="brand" style="left:60px;top:92px;width:140px;font-size:13px"><span class="mark" style="width:30px;height:30px"></span>MERIVALE<span style="font-size:6px;font-weight:400">LAW FIRM PC</span></div>
    <div class="abs" style="left:240px;top:60px;width:2px;height:180px;background:var(--mist)"></div>
    <div class="abs" style="left:264px;top:66px;font-size:10px;font-weight:800;color:var(--blue)">GET IN TOUCH</div>
    <div class="abs contact-list" style="left:264px;top:90px;font-size:6.5px;line-height:26px">
      <div><svg width="9" height="9" viewBox="0 0 24 24"><path fill="currentColor" d="M6.6 10.8a15 15 0 006.6 6.6l2.2-2.2c.3-.3.7-.4 1-.2 1.1.4 2.3.6 3.6.6.6 0 1 .4 1 1V20c0 .6-.4 1-1 1A17 17 0 013 4c0-.6.4-1 1-1h3.5c.6 0 1 .4 1 1 0 1.3.2 2.5.6 3.6.1.3 0 .7-.2 1z"/></svg> <span>(555) 014-2280</span></div>
      <div><svg width="9" height="9" viewBox="0 0 24 24"><path fill="currentColor" d="M2 5h20v14H2zm2 2v.5l8 5 8-5V7z"/></svg> <span>info@merivalelaw.com</span></div>
      <div><svg width="9" height="9" viewBox="0 0 24 24"><path fill="currentColor" d="M12 2a10 10 0 100 20 10 10 0 000-20zm0 2c1.5 1.8 2.4 4.3 2.5 7h-5c.1-2.7 1-5.2 2.5-7zM4.1 13h3.4c.1 2.3.7 4.4 1.6 6A8 8 0 014.1 13zm0-2a8 8 0 015-6c-.9 1.6-1.5 3.7-1.6 6zm5.4 2h5c-.1 2.7-1 5.2-2.5 7-1.5-1.8-2.4-4.3-2.5-7zm7 0h3.4a8 8 0 01-5 6c.9-1.6 1.5-3.7 1.6-6zm0-2c-.1-2.3-.7-4.4-1.6-6a8 8 0 015 6z"/></svg> <span>www.merivalelaw.com</span></div>
      <div><svg width="9" height="9" viewBox="0 0 24 24"><path fill="currentColor" d="M12 2a7 7 0 017 7c0 5-7 13-7 13S5 14 5 9a7 7 0 017-7zm0 4a3 3 0 100 6 3 3 0 000-6z"/></svg> <span>120 Harbor Street, Suite 400, Boston, MA</span></div>
    </div>
    <div class="corner br" style="right:14px;bottom:14px"></div>
  </div>
</section>

</body>
</html>
```